Team email banner for internal communications

We need a team email banner/header that will be applied to all internal communications from our department to other functions. The graphic should be optimized for Outlook and be landscape in layout. We have 5 different silo within our team and will need so will either need have a blank space to denote each team or have change in colors/graphics to denote each team (see current headers attached to job description). We are looking for a banner that combines our team logo (attached) with our team name, Regional Talent & Coaching Unit. The theme should be L&D and pharmaceutical in nature.

Need extra days to review

The text in the banner should be Regional Talent & Coaching Unit with the team logo (attached).

```html
<!DOCTYPE html>
<html lang="en">
<head>
<meta charset="utf-8">
<title>Regional Talent &amp; Coaching Unit – Email Banners</title>
<link rel="stylesheet" href="https://fonts.googleapis.com/css2?family=Montserrat:wght@700&family=Roboto:ital,wght@1,500&display=swap">
<style>
  :root {
    --ink: #0a0a0a;
    --paper: #ffffff;
    --brand-red: #e0261f;
    --heme-dark: #b0242c;  --heme-light: #ee1f26;
    --tumor-dark: #4a2650; --tumor-light: #7e3f8f; --tumor-text: #7a3b8c;
    --lead-dark: #d42a22;  --lead-light: #f04640;
    --market-dark: #2c4356; --market-light: #3e7aa0; --market-text: #3d6f96;
    --ops-dark: #0f5f9c;   --ops-light: #1b8ad3;
  }
  html, body { margin: 0; padding: 0; overflow: hidden; }
  body { width: 800px; height: 1200px; background: var(--paper); position: relative; }
  .banner { position: absolute; display: block; }
  .banner--overview { left: 67px; top: 35px; width: 666px; height: 222px; --dark: var(--heme-dark); --light: var(--heme-light); --accent: var(--heme-dark); }
  .banner--team { left: 198px; width: 401px; height: 133px; }
  .banner--hematology { top: 301px; --dark: var(--heme-dark); --light: var(--heme-light); --accent: var(--heme-dark); --label: var(--heme-dark); }
  .banner--tumor { top: 477px; --dark: var(--tumor-dark); --light: var(--tumor-light); --accent: var(--tumor-dark); --label: var(--tumor-text); }
  .banner--leadership { top: 653px; --dark: var(--lead-dark); --light: var(--lead-light); --accent: var(--lead-dark); --label: var(--lead-light); }
  .banner--market { top: 829px; --dark: var(--market-dark); --light: var(--market-light); --accent: var(--market-dark); --label: var(--market-text); }
  .banner--ops { top: 1005px; --dark: var(--ops-dark); --light: var(--ops-light); --accent: var(--ops-dark); --label: var(--ops-light); }

  .band-dark { fill: var(--dark); }
  .band-light { fill: var(--light); }
  .band-accent { fill: var(--accent); }
  .swoosh { fill: var(--ink); }
  .brand-mark { fill: var(--brand-red); }
  .photo-frame { fill: none; stroke: var(--accent); stroke-width: 2; }
  .team-name { font-family: "Montserrat", sans-serif; font-weight: 700; fill: var(--ink); }
  .team-label { font-family: "Roboto", sans-serif; font-style: italic; font-weight: 500; fill: var(--label); }
  .silo { font-family: "Roboto", sans-serif; font-style: italic; font-weight: 500; font-size: 20px; }
  .silo--heme { fill: var(--heme-dark); }
  .silo--tumor { fill: var(--tumor-text); }
  .silo--lead { fill: var(--lead-light); }
  .silo--market { fill: var(--market-text); }
  .silo--ops { fill: var(--ops-light); }
  .ring { fill: none; stroke: var(--ink); stroke-width: 9; }
</style>
</head>
<body>

<!-- Overview header -->
<svg class="banner banner--overview" viewBox="0 0 1000 334" xmlns="http://www.w3.org/2000/svg">
  <defs>
    <radialGradient id="ov-heme"><stop offset="0" stop-color="#e0474c"/><stop offset="1" stop-color="#8e1218"/></radialGradient>
    <radialGradient id="ov-tumor"><stop offset="0" stop-color="#a23a8c"/><stop offset="1" stop-color="#1e1630"/></radialGradient>
    <radialGradient id="ov-lead"><stop offset="0" stop-color="#d8dadf"/><stop offset="1" stop-color="#7d8794"/></radialGradient>
    <radialGradient id="ov-market"><stop offset="0" stop-color="#f0a450"/><stop offset="1" stop-color="#3b4a66"/></radialGradient>
    <radialGradient id="ov-ops"><stop offset="0" stop-color="#e8dcc3"/><stop offset="1" stop-color="#8fa6bf"/></radialGradient>
  </defs>
  <rect width="1000" height="334" fill="#fff"/>
  <path class="band-dark" d="M0,145 Q250,175 450,250 Q700,330 1000,300 V334 H0 Z"/>
  <path class="band-light" d="M0,262 Q220,272 430,334 H0 Z"/>
  <path class="swoosh" d="M300,228 Q620,320 1000,252 V292 Q700,355 380,272 Z"/>
  <path class="swoosh" d="M0,0 H210 Q80,30 0,128 Z"/>
  <path class="band-accent" d="M770,0 H1000 V98 Q900,28 770,0 Z"/>
  <path class="swoosh" d="M815,0 H1000 V82 Q925,22 815,0 Z"/>

  <circle class="ring" cx="218" cy="186" r="100"/>
  <g stroke="#fff" stroke-width="3">
    <circle cx="218" cy="93" r="41" fill="url(#ov-heme)" role="img" aria-label="Photo: red blood cells"/>
    <circle cx="309" cy="157" r="41" fill="url(#ov-tumor)" role="img" aria-label="Photo: tumour cell"/>
    <circle cx="275" cy="264" r="41" fill="url(#ov-lead)" role="img" aria-label="Photo: team hands joined together"/>
    <circle cx="162" cy="264" r="41" fill="url(#ov-market)" role="img" aria-label="Photo: business handshake"/>
    <circle cx="128" cy="157" r="41" fill="url(#ov-ops)" role="img" aria-label="Illustration: people running on gears"/>
  </g>

  <circle class="brand-mark" cx="505" cy="112" r="34"/>
  <text class="team-name" x="940" y="92" font-size="46" text-anchor="end">Regional Talent</text>
  <text class="team-name" x="940" y="145" font-size="46" text-anchor="end">&amp; Coaching Unit</text>
  <text class="silo silo--heme" x="588" y="190">- Hematology</text>
  <text class="silo silo--tumor" x="752" y="190">- Solid Tumor</text>
  <text class="silo silo--lead" x="588" y="215">- Leadership Development</text>
  <text class="silo silo--market" x="588" y="241">- Market Acces</text>
  <text class="silo silo--ops" x="752" y="241">- Operations &amp; Capabilities</text>
</svg>

<!-- Team banners -->
<svg class="banner banner--team banner--hematology" viewBox="0 0 601 200" xmlns="http://www.w3.org/2000/svg">
  <defs><radialGradient id="ph-heme"><stop offset="0" stop-color="#e0474c"/><stop offset="1" stop-color="#8e1218"/></radialGradient></defs>
  <rect width="601" height="200" fill="#fff"/>
  <path class="band-dark" d="M0,88 Q160,105 300,165 Q450,215 601,195 V200 H0 Z"/>
  <path class="band-light" d="M0,150 Q180,160 280,200 H0 Z"/>
  <path class="swoosh" d="M200,145 Q420,192 601,152 V188 Q430,212 255,168 Z"/>
  <path class="swoosh" d="M0,0 H125 Q40,18 0,48 Z"/>
  <path class="band-accent" d="M462,0 H601 V56 Q540,14 462,0 Z"/>
  <path class="swoosh" d="M490,0 H601 V44 Q552,10 490,0 Z"/>
  <circle cx="132" cy="108" r="75" fill="url(#ph-heme)" stroke="#fff" stroke-width="3" role="img" aria-label="Photo: red blood cells"/>
  <circle class="photo-frame" cx="132" cy="108" r="77"/>
  <circle class="brand-mark" cx="290" cy="72" r="22"/>
  <text class="team-name" x="563" y="62" font-size="28" text-anchor="end">Regional Talent</text>
  <text class="team-name" x="563" y="94" font-size="28" text-anchor="end">&amp; Coaching Unit</text>
  <text class="team-label" x="563" y="136" font-size="28" text-anchor="end">Hematology</text>
</svg>

<svg class="banner banner--team banner--tumor" viewBox="0 0 601 200" xmlns="http://www.w3.org/2000/svg">
  <defs><radialGradient id="ph-tumor"><stop offset="0" stop-color="#a23a8c"/><stop offset="1" stop-color="#1e1630"/></radialGradient></defs>
  <rect width="601" height="200" fill="#fff"/>
  <path class="band-dark" d="M0,88 Q160,105 300,165 Q450,215 601,195 V200 H0 Z"/>
  <path class="band-light" d="M0,150 Q180,160 280,200 H0 Z"/>
  <path class="swoosh" d="M200,145 Q420,192 601,152 V188 Q430,212 255,168 Z"/>
  <path class="swoosh" d="M0,0 H125 Q40,18 0,48 Z"/>
  <path class="band-accent" d="M462,0 H601 V56 Q540,14 462,0 Z"/>
  <path class="swoosh" d="M490,0 H601 V44 Q552,10 490,0 Z"/>
  <circle cx="132" cy="108" r="75" fill="url(#ph-tumor)" stroke="#fff" stroke-width="3" role="img" aria-label="Photo: tumour cell"/>
  <circle class="photo-frame" cx="132" cy="108" r="77"/>
  <circle class="brand-mark" cx="290" cy="72" r="22"/>
  <text class="team-name" x="563" y="62" font-size="28" text-anchor="end">Regional Talent</text>
  <text class="team-name" x="563" y="94" font-size="28" text-anchor="end">&amp; Coaching Unit</text>
  <text class="team-label" x="563" y="136" font-size="28" text-anchor="end">Solid Tumor</text>
</svg>

<svg class="banner banner--team banner--leadership" viewBox="0 0 601 200" xmlns="http://www.w3.org/2000/svg">
  <defs><radialGradient id="ph-lead"><stop offset="0" stop-color="#d8dadf"/><stop offset="1" stop-color="#7d8794"/></radialGradient></defs>
  <rect width="601" height="200" fill="#fff"/>
  <path class="band-dark" d="M0,88 Q160,105 300,165 Q450,215 601,195 V200 H0 Z"/>
  <path class="band-light" d="M0,150 Q180,160 280,200 H0 Z"/>
  <path class="swoosh" d="M200,145 Q420,192 601,152 V188 Q430,212 255,168 Z"/>
  <path class="swoosh" d="M0,0 H125 Q40,18 0,48 Z"/>
  <path class="band-accent" d="M462,0 H601 V56 Q540,14 462,0 Z"/>
  <path class="swoosh" d="M490,0 H601 V44 Q552,10 490,0 Z"/>
  <circle cx="132" cy="108" r="75" fill="url(#ph-lead)" stroke="#fff" stroke-width="3" role="img" aria-label="Photo: team hands joined together"/>
  <circle class="photo-frame" cx="132" cy="108" r="77"/>
  <circle class="brand-mark" cx="290" cy="72" r="22"/>
  <text class="team-name" x="563" y="62" font-size="28" text-anchor="end">Regional Talent</text>
  <text class="team-name" x="563" y="94" font-size="28" text-anchor="end">&amp; Coaching Unit</text>
  <text class="team-label" x="563" y="128" font-size="21" text-anchor="end">Leadership Development</text>
</svg>

<svg class="banner banner--team banner--market" viewBox="0 0 601 200" xmlns="http://www.w3.org/2000/svg">
  <defs><radialGradient id="ph-market"><stop offset="0" stop-color="#f0a450"/><stop offset="1" stop-color="#3b4a66"/></radialGradient></defs>
  <rect width="601" height="200" fill="#fff"/>
  <path class="band-dark" d="M0,88 Q160,105 300,165 Q450,215 601,195 V200 H0 Z"/>
  <path class="band-light" d="M0,150 Q180,160 280,200 H0 Z"/>
  <path class="swoosh" d="M200,145 Q420,192 601,152 V188 Q430,212 255,168 Z"/>
  <path class="swoosh" d="M0,0 H125 Q40,18 0,48 Z"/>
  <path class="band-accent" d="M462,0 H601 V56 Q540,14 462,0 Z"/>
  <path class="swoosh" d="M490,0 H601 V44 Q552,10 490,0 Z"/>
  <circle cx="132" cy="108" r="75" fill="url(#ph-market)" stroke="#fff" stroke-width="3" role="img" aria-label="Photo: business handshake"/>
  <circle class="photo-frame" cx="132" cy="108" r="77"/>
  <circle class="brand-mark" cx="290" cy="72" r="22"/>
  <text class="team-name" x="563" y="62" font-size="28" text-anchor="end">Regional Talent</text>
  <text class="team-name" x="563" y="94" font-size="28" text-anchor="end">&amp; Coaching Unit</text>
  <text class="team-label" x="563" y="138" font-size="30" text-anchor="end">Market Acces</text>
</svg>

<svg class="banner banner--team banner--ops" viewBox="0 0 601 200" xmlns="http://www.w3.org/2000/svg">
  <defs><radialGradient id="ph-ops"><stop offset="0" stop-color="#e8dcc3"/><stop offset="1" stop-color="#8fa6bf"/></radialGradient></defs>
  <rect width="601" height="200" fill="#fff"/>
  <path class="band-dark" d="M0,88 Q160,105 300,165 Q450,215 601,195 V200 H0 Z"/>
  <path class="band-light" d="M0,150 Q180,160 280,200 H0 Z"/>
  <path class="swoosh" d="M200,145 Q420,192 601,152 V188 Q430,212 255,168 Z"/>
  <path class="swoosh" d="M0,0 H125 Q40,18 0,48 Z"/>
  <path class="band-accent" d="M462,0 H601 V56 Q540,14 462,0 Z"/>
  <path class="swoosh" d="M490,0 H601 V44 Q552,10 490,0 Z"/>
  <circle cx="132" cy="108" r="75" fill="url(#ph-ops)" stroke="#fff" stroke-width="3" role="img" aria-label="Illustration: people running on gears"/>
  <circle class="photo-frame" cx="132" cy="108" r="77"/>
  <circle class="brand-mark" cx="290" cy="72" r="22"/>
  <text class="team-name" x="563" y="62" font-size="28" text-anchor="end">Regional Talent</text>
  <text class="team-name" x="563" y="94" font-size="28" text-anchor="end">&amp; Coaching Unit</text>
  <text class="team-label" x="563" y="128" font-size="21" text-anchor="end">Operations &amp; Capabilities</text>
</svg>

</body>
</html>
```